Granite Ridge Holdings

I have a real estate investment business.

** I need editable vector files of the final design.

Industry/Entity Type

Real Estate

Contact Information for Business Card

I would like the card to be clear and direct with the company name and contact info. I would prefer not to have a design that is too busy (i.e., with excessive detail) in the business card.

Font styles to use
Sans Serif

Requirements
Must have
• My card must have the following information listed below:
• Company name: Grainite Ridge Holdings LLC
• My name: Daniel Vorsley
• Phone number: (555) 218-9067
• Email address: dtvorsley@mailbox-example.net
• Keywords: “Real Estate Investments”
Nice to have
• I would like to have a design that resembles the characteristics/uses of obsidian stone which resembles something related to strength and resilience. Perhaps something with sharp, sleek color transitions as well.

```html
<!DOCTYPE html>
<html lang="en">
<head>
<meta charset="utf-8">
<title>Granite Ridge Holdings – Business Card</title>
<link rel="stylesheet" href="https://fonts.googleapis.com/css2?family=Outfit:wght@300;500;600&display=swap">
<style>
  :root {
    --backdrop: #8e8e90;
    --card: #ffffff;
    --ink: #0a0a0a;
    --stone-dark: #0c0c0d;
    --stone-mid: #1e1e20;
    --stone-light: #3e3e40;
  }
  html, body {
    margin: 0;
    width: 1200px;
    height: 1000px;
    overflow: hidden;
    background: var(--backdrop);
    font-family: "Outfit", sans-serif;
  }
  .card {
    position: absolute;
    left: 195px;
    top: 267px;
    width: 810px;
    height: 462px;
    background: var(--card);
    overflow: hidden;
    color: var(--ink);
  }
  .stone-facets {
    position: absolute;
    left: 0;
    top: 0;
  }
  .holder-name {
    position: absolute;
    left: 30px;
    top: 72px;
    margin: 0;
    font-size: 45px;
    font-weight: 600;
    letter-spacing: -0.5px;
    line-height: 1;
  }
  .name-rule {
    position: absolute;
    left: 30px;
    top: 134px;
    width: 491px;
    height: 6px;
    background: var(--ink);
  }
  .company-name {
    position: absolute;
    left: 30px;
    top: 158px;
    margin: 0;
    font-size: 34px;
    font-weight: 500;
    line-height: 1;
  }
  .tagline {
    position: absolute;
    left: 30px;
    top: 201px;
    margin: 0;
    font-size: 22px;
    font-weight: 300;
    line-height: 1;
  }
  .contact {
    position: absolute;
    left: 29px;
    margin: 0;
    display: flex;
    align-items: center;
    gap: 8px;
    font-weight: 500;
    line-height: 1;
  }
  .contact--phone { top: 342px; font-size: 25px; }
  .contact--email { top: 396px; font-size: 19px; }
  .contact svg { flex: none; fill: var(--ink); }
</style>
</head>
<body>
  <div class="card">
    <svg class="stone-facets" width="810" height="462" viewBox="0 0 810 462" role="img" aria-label="Faceted obsidian stone motif in black and charcoal tones">
      <defs>
        <linearGradient id="obsidian" x1="0" y1="0" x2="1" y2="1">
          <stop offset="0" stop-color="var(--stone-mid)"/>
          <stop offset="0.45" stop-color="var(--stone-dark)"/>
          <stop offset="0.75" stop-color="var(--stone-light)"/>
          <stop offset="1" stop-color="var(--stone-mid)"/>
        </linearGradient>
      </defs>
      <polygon points="578,0 810,0 810,462 365,462 455,301 648,256 613,141 635,30" fill="url(#obsidian)"/>
    </svg>

    <h1 class="holder-name">Daniel Vorsley</h1>
    <div class="name-rule"></div>
    <p class="company-name">Grainite Ridge Holdings LLC</p>
    <p class="tagline">Real Estate Investments</p>

    <p class="contact contact--phone">
      <svg width="22" height="34" viewBox="0 0 22 34" aria-hidden="true">
        <path d="M7 1 L11 1 L12 9 L9 11 C8 15 9 20 11 24 L14 23 L18 30 L14 33 C6 32 2 22 2 14 C2 8 4 3 7 1 Z"/>
      </svg>
      <span>(555) 218-9067</span>
    </p>
    <p class="contact contact--email">
      <svg width="32" height="22" viewBox="0 0 32 22" aria-hidden="true">
        <path d="M0 0 H32 V22 H0 Z M3 3 L16 13 L29 3 Z M2 5 V20 L11 12 Z M30 5 V20 L21 12 Z M13 14 L4 20 H28 L19 14 L16 16 Z" fill-rule="evenodd"/>
      </svg>
      <span>dtvorsley@mailbox-example.net</span>
    </p>
  </div>
</body>
</html>
```